Marketplace Web Re-design overhaul @quarrynest

Hi,
We are currently in production with a website that is getting some mixed feedback about visual appeal and usability. We are using a responsive design and need to stay true to the logo colours and other marketing collateral we have in place. I will provide a brochure with the colour palate we use for some guidance. If you can please help us design something fresh and modern to communicate the essence of our company. The brochure will be a good summary of what we do and who we are targeting as customers. Our current website can be found at www.quarrynest.com. If there is any questions, please let me know.

Target Market(s)

Contractors and Corporate Companies

Industry/Entity Type

Information Technology

Number of Pages Required

4 page

Requirements
Must have
• Must have a complete new visual look, including
• 1. Images
• 2. Background colour scheme overhaul (not black)
• 3. re-design of the layout but keep to similar page breakdowns
Nice to have
• Some of the pages are a bit wordy, happy to have suggestions on how to reduce.
• Would be great if we can integrate the Plumb.ON! blog page to the Quarrynest page?
• This is some feedback a fellow UX designer provided to improve our CRO
• First off when you land on the home page, who is your audience? Are you everything to everyone? Even after watching the video (https://www.vidmarrow.net/watch?v=q7RtPe3LwZ0), I do not know what markets you service or who this app will be for.
• Your main headline and paragraph above the fold I find unnecessarily wordy and an overuse of 'buzzwords' . Perhaps you could look at appealing to the lowest common denominator and make it very simple and put it all into a simple sentence.
• The main hero image to the right of the headline offers no emotional pull at all. I'm assuming it's just a screenshot of your dashboard? Personally, I would be looking at using a person's image in that space.
• Also in this space, increase the size of your 'register' button. On the topic of your register button, you have it in different colours. Green in header, and red in content. Make it the same colour, and don't use that colour again on the site. That colour is to become your call to action (CTA) colour. Understandably you'll have three different colours for the account type, and again, don't use these colours anywhere else on the site.
• The registration area where the three account types are where you choose which one suits you, it's extremely busy with background images and heavy use of text. If you were my client, I would be advising you to ditch the bg image (including the Zelo shot), keeping the text, making the register icons much bigger. Perhaps instead of bg images, use a solid colour for each (green, orange, red). I'm highly confident this change will make a massive difference in your sign up rate.
Should not have
• Please keep to the fonts used on the original website
• Keep to the colour provided on the company brochure for guidance.

```html
<!DOCTYPE html>
<html lang="en">
<head>
<meta charset="utf-8">
<title>Quarrynest – Available, Quality Talent on Demand</title>
<link rel="stylesheet" href="https://fonts.googleapis.com/css2?family=Arimo:wght@400;700&family=Open+Sans:wght@400;600;700&family=Roboto+Condensed:wght@400;700&display=swap">
<style>
  :root{
    --red:#c62232;
    --red-soft:#d94a52;
    --green:#139a48;
    --green-card:#3aa655;
    --orange:#f05a36;
    --ink:#222;
    --grey-card:#e3e3e3;
    --black:#000;
    --white:#fff;
  }
  *{box-sizing:border-box;margin:0;padding:0}
  html,body{width:1200px;height:3158px;overflow:hidden}
  body{font-family:"Open Sans",Arial,sans-serif;color:var(--ink);background:var(--white);position:relative}
  a{color:inherit;text-decoration:none}
  .wrap{width:1044px;margin:0 auto;position:relative}

  /* hero */
  .hero{height:625px;position:relative;overflow:hidden}
  .hero-photo{position:absolute;inset:0;background:linear-gradient(100deg,#3a3c40 0%,#5a5c60 35%,#6b6d70 55%,#3c3e43 80%,#2a2c30 100%)}
  .hero-shade{position:absolute;inset:0;background:rgba(30,30,35,.35)}
  .brand{position:absolute;left:78px;top:20px;display:flex;align-items:center;gap:10px;color:var(--white);font-size:28px;font-weight:400}
  .brand-dot{width:24px;height:24px;border-radius:50%;background:var(--red)}
  .hero h1{position:absolute;top:272px;left:0;right:0;text-align:center;font-family:"Arimo",Arial,sans-serif;font-weight:400;font-size:52px;color:var(--white)}
  .btn{display:inline-flex;align-items:center;justify-content:center;background:var(--red);color:var(--white);text-transform:uppercase;font-family:"Open Sans",Arial,sans-serif}
  .btn-join{position:absolute;left:507px;top:354px;width:185px;height:71px;font-size:23px;border-radius:2px}

  /* nav */
  .main-nav{height:63px;background:var(--green)}
  .main-nav ul{list-style:none;display:flex;height:63px;width:1044px;margin:0 auto}
  .main-nav li{height:63px;display:flex;align-items:center;padding:0 26px;color:var(--white);font-size:15px;text-transform:uppercase}
  .main-nav li:first-child{padding:0 20px}
  .main-nav li + li{margin-left:26px;padding:0 0}
  .main-nav li + li + li,.main-nav li + li + li + li,.main-nav li:last-child{margin-left:52px}
  .main-nav .active{background:var(--red)}

  /* welcome */
  .welcome{height:322px;position:relative;text-align:center;overflow:hidden}
  .welcome-photo{position:absolute;inset:0;background:linear-gradient(90deg,#c9cbcd 0%,#eceded 30%,#f2f2f2 55%,#dfe1e3 80%,#cfd2d5 100%)}
  .welcome-inner{position:relative;padding-top:46px}
  .welcome h2{font-family:"Roboto Condensed",Arial,sans-serif;font-weight:400;font-size:46px;color:var(--green);line-height:1}
  .welcome p{font-size:15.5px;line-height:26px;width:980px;margin:12px auto 0;color:#222}
  .welcome p + p{margin-top:22px}
  .btn-know{width:166px;height:53px;font-size:16px;margin-top:10px}

  /* services */
  .section-title{font-family:"Roboto Condensed",Arial,sans-serif;font-weight:400;font-size:40px;color:var(--green);text-align:center}
  .services{padding-top:56px}
  .service-grid{display:flex;justify-content:space-between;margin-top:20px}
  .service{width:310px;height:339px;color:var(--white);text-align:center;padding:48px 22px 0}
  .service--red{background:var(--red)}
  .service--green{background:var(--green-card)}
  .service--orange{background:var(--orange)}
  .service svg{width:48px;height:48px}
  .service h3{font-family:"Roboto Condensed",Arial,sans-serif;font-weight:400;font-size:22px;margin-top:22px;text-transform:uppercase}
  .service p{font-size:14.5px;line-height:23px;margin-top:12px}
  .more-link{display:inline-block;margin-top:14px;font-size:14.5px;text-decoration:underline;text-transform:uppercase}

  /* audience rows */
  .audience{margin-top:38px}
  .audience-row{display:flex;justify-content:space-between}
  .audience-row + .audience-row{margin-top:12px}
  .photo{height:333px}
  .photo--man{width:509px;background:linear-gradient(90deg,#9aa7b1 0%,#c8d0d5 45%,#7b7f86 70%,#b4bcc2 100%)}
  .photo--desk{width:518px;background:linear-gradient(180deg,#4b5058 0%,#9ea5ac 40%,#e4e6e8 70%,#cfd3d6 100%)}
  .panel{height:333px;color:var(--white);padding:0 0 0 26px}
  .panel--red{width:520px;background:var(--red);padding-top:0}
  .panel--green{width:513px;background:var(--green-card);padding-left:0}
  .panel h3{font-family:"Roboto Condensed",Arial,sans-serif;font-weight:400;font-size:41px;text-transform:uppercase;line-height:1}
  .panel--red h3{margin:6px 0 0 -6px;font-size:40px}
  .panel ul{list-style:none;margin-top:22px}
  .panel--green ul{padding-left:2px}
  .panel li{display:flex;align-items:flex-start;gap:14px;font-size:17px;line-height:18px;margin-bottom:18px}
  .panel li svg{flex:none;width:20px;height:20px;margin-top:-1px}
  .panel--red .btn-more{background:var(--green);margin-left:0}
  .panel--green .btn-more{background:var(--red);margin-left:0}
  .btn-more{width:147px;height:50px;font-size:16px;margin-top:6px}

  /* newsletter */
  .newsletter{height:155px;margin-top:53px;position:relative;overflow:hidden}
  .newsletter-photo{position:absolute;inset:0;background:linear-gradient(90deg,#c93a42 0%,#d4545a 45%,#c9444b 100%)}
  .newsletter-inner{position:relative;width:1044px;margin:0 auto;height:155px}
  .newsletter h2{position:absolute;left:132px;top:46px;font-family:"Open Sans",Arial,sans-serif;font-weight:700;font-size:36px;color:var(--white);letter-spacing:.5px;line-height:1}
  .newsletter p{position:absolute;left:80px;top:95px;font-size:13.5px;color:var(--white)}
  .newsletter-field{position:absolute;left:452px;top:50px;width:333px;height:51px;border:2px solid var(--white);color:var(--white);font-size:14px;padding:14px 8px;font-family:"Open Sans",Arial,sans-serif}
  .btn-subscribe{position:absolute;left:798px;top:50px;width:166px;height:51px;background:var(--green);font-weight:700;font-size:16px}

  /* team */
  .team{padding-top:58px}
  .team-grid{display:flex;justify-content:space-between;margin-top:32px}
  .member{width:314px;height:299px;background:var(--grey-card);border:1px solid #d0d0d0;text-align:center;padding-top:10px}
  .member-photo{width:156px;height:156px;border-radius:50%;border:2px solid var(--red);margin:0 auto;background:linear-gradient(180deg,#f4f4f4 0%,#c4c7ca 55%,#7d8187 100%)}
  .member h3{font-size:18px;font-weight:700;margin-top:22px}
  .member p{font-size:15px;margin-top:6px}

  /* footer */
  .site-footer{position:absolute;left:0;top:2823px;width:1200px;height:288px;background:var(--black);color:var(--white)}
  .footer-links{position:absolute;left:78px;top:32px;list-style:none;font-size:14.5px}
  .footer-links li{height:36.5px}
  .contact{position:absolute;left:452px;top:40px;list-style:none;font-size:14.5px}
  .contact li{display:flex;align-items:flex-start;gap:14px;width:270px;line-height:26px}
  .contact li + li{margin-top:20px}
  .contact .ico{flex:none;width:50px;height:50px;border-radius:50%;background:var(--white);display:flex;align-items:center;justify-content:center}
  .contact .ico svg{width:22px;height:22px}
  .contact li:nth-child(2),.contact li:nth-child(3){align-items:center}
  .partners{position:absolute;left:836px;top:30px}
  .partners h2{font-family:"Roboto Condensed",Arial,sans-serif;font-weight:400;font-size:33px}
  .badge-a{width:155px;height:78px;margin-top:14px;display:flex}
  .badge-a span:first-child{width:78px;background:#2a2a2a}
  .badge-a span:last-child{width:77px;background:var(--red)}
  .badge-b{display:flex;align-items:center;gap:8px;margin-top:20px}
  .badge-b .disc{width:72px;height:72px;border-radius:50%;background:#2a6fa8}
  .badge-b .bar{width:136px;height:36px;background:#2a6fa8}
  .copyright{position:absolute;left:0;top:3111px;width:1200px;height:47px;background:var(--red);color:var(--white);text-align:center;font-size:14px;line-height:47px}
  .copyright strong{font-weight:700}
</style>
</head>
<body>

<header class="hero">
  <div class="hero-photo" role="img" aria-label="Photo of smiling colleagues working together at a laptop"></div>
  <div class="hero-shade"></div>
  <div class="brand"><span class="brand-dot"></span>quarrynest</div>
  <h1>Available, Quality Talent on Demand!</h1>
  <a class="btn btn-join" href="#">Join Now</a>
</header>

<nav class="main-nav">
  <ul>
    <li class="active">Home</li>
    <li>How it works</li>
    <li>About us</li>
    <li>Our partners</li>
    <li>Blog</li>
  </ul>
</nav>

<section class="welcome">
  <div class="welcome-photo" role="img" aria-label="Faded photo of a hand reaching into a connected network of people icons"></div>
  <div class="welcome-inner">
    <h2>WELCOME TO QUARRYNEST</h2>
    <p>Quarrynest is a unique marketplace providing contractors and companies a platform to connect in real-time by exposing the "availability status". Through intuitive search Quarrynest will instantly shortlist available contractors with matching skill criteria.</p>
    <p>This is an invaluable tool for companies finding the right people at the right time and at low cost!!</p>
    <a class="btn btn-know" href="#">Know More</a>
  </div>
</section>

<section class="services wrap">
  <h2 class="section-title">SERVICES</h2>
  <div class="service-grid">
    <article class="service service--red">
      <svg viewBox="0 0 48 48" fill="#fff" aria-hidden="true">
        <circle cx="24" cy="12" r="6"/><circle cx="11" cy="16" r="4.5"/><circle cx="37" cy="16" r="4.5"/>
        <path d="M16 22h16v14h-4v8h-8v-8h-4z"/><path d="M5 23h10v10h-2v7H7v-7H5z"/><path d="M33 23h10v10h-2v7h-6v-7h-2z"/>
      </svg>
      <h3>Skills Match</h3>
      <p>Quarrynest has a secret sauce to find the right people to match the job requirements.</p>
      <a class="more-link" href="#">More Info</a>
    </article>
    <article class="service service--green">
      <svg viewBox="0 0 48 48" fill="none" stroke="#fff" stroke-width="2.5" aria-hidden="true">
        <rect x="6" y="9" width="36" height="33" rx="2"/><path d="M14 5v8M34 5v8M6 17h36"/>
        <g fill="#fff" stroke="none"><rect x="12" y="22" width="5" height="4"/><rect x="21.5" y="22" width="5" height="4"/><rect x="31" y="22" width="5" height="4"/><rect x="12" y="31" width="5" height="4"/><rect x="21.5" y="31" width="5" height="4"/><rect x="31" y="31" width="5" height="4"/></g>
      </svg>
      <h3>Calendar</h3>
      <p>Uniquely Quarrynest has the visibility of contractors availability to work on projects.</p>
      <a class="more-link" href="#">More Info</a>
    </article>
    <article class="service service--orange">
      <svg viewBox="0 0 48 48" aria-hidden="true">
        <path fill="#fff" d="M24 3c-8 0-14 6-14 14 0 10 14 28 14 28s14-18 14-28c0-8-6-14-14-14z"/>
        <circle cx="24" cy="17" r="5" fill="#f05a36"/>
      </svg>
      <h3>Locations</h3>
      <p>Coupled with the skills &amp; availability the locations map you to the resources closest to the job.</p>
      <a class="more-link" href="#">More Info</a>
    </article>
  </div>
</section>

<section class="audience wrap">
  <div class="audience-row">
    <div class="photo photo--man" role="img" aria-label="Photo of a smiling businessman in a suit in a bright office"></div>
    <div class="panel panel--red">
      <h3>Quarrynest for Companies</h3>
      <ul>
        <li><svg viewBox="0 0 20 20" fill="none" stroke="#fff" stroke-width="2"><rect x="2" y="4" width="13" height="13"/><path d="M5 10l4 4 9-10"/></svg>Increase utilisation by reducing idle time.</li>
        <li><svg viewBox="0 0 20 20" fill="none" stroke="#fff" stroke-width="2"><rect x="2" y="4" width="13" height="13"/><path d="M5 10l4 4 9-10"/></svg>Choice of work based on offers received.</li>
        <li><svg viewBox="0 0 20 20" fill="none" stroke="#fff" stroke-width="2"><rect x="2" y="4" width="13" height="13"/><path d="M5 10l4 4 9-10"/></svg>Increase earning potential by dealing direct<br>with companie</li>
      </ul>
      <a class="btn btn-more" href="#">More Info</a>
    </div>
  </div>
  <div class="audience-row">
    <div class="panel panel--green">
      <h3>Quarrynest for Contractor</h3>
      <ul>
        <li><svg viewBox="0 0 20 20" fill="none" stroke="#fff" stroke-width="2"><rect x="2" y="4" width="13" height="13"/><path d="M5 10l4 4 9-10"/></svg>Save time by reviewing qualified shortlist of skills<br>&amp; availability.</li>
        <li><svg viewBox="0 0 20 20" fill="none" stroke="#fff" stroke-width="2"><rect x="2" y="4" width="13" height="13"/><path d="M5 10l4 4 9-10"/></svg>Predictable market talent pools and access to<br>active resources.</li>
        <li><svg viewBox="0 0 20 20" fill="none" stroke="#fff" stroke-width="2"><rect x="2" y="4" width="13" height="13"/><path d="M5 10l4 4 9-10"/></svg>Negotiate rates directly with the contractor.</li>
      </ul>
      <a class="btn btn-more" href="#">More Info</a>
    </div>
    <div class="photo photo--desk" role="img" aria-label="Photo of a pen resting on paperwork on an office desk"></div>
  </div>
</section>

<section class="newsletter">
  <div class="newsletter-photo" role="img" aria-label="Red tinted photo of hands typing on a keyboard"></div>
  <div class="newsletter-inner">
    <h2>NEWSLETTER</h2>
    <p>Subscribe to our newsletter for latest updates.</p>
    <div class="newsletter-field">Enter your mail</div>
    <a class="btn btn-subscribe" href="#">Subscribe</a>
  </div>
</section>

<section class="team wrap">
  <h2 class="section-title">OUR TEAM</h2>
  <div class="team-grid">
    <article class="member"><div class="member-photo" role="img" aria-label="Portrait of a team member at a desk"></div><h3>Name</h3><p>Lorem ipsum dolor sit amet</p></article>
    <article class="member"><div class="member-photo" role="img" aria-label="Portrait of a team member with a laptop"></div><h3>Name</h3><p>Lorem ipsum dolor sit amet</p></article>
    <article class="member"><div class="member-photo" role="img" aria-label="Portrait of a team member working on a laptop"></div><h3>Name</h3><p>Lorem ipsum dolor sit amet</p></article>
  </div>
</section>

<footer class="site-footer">
  <ul class="footer-links">
    <li>Home</li><li>How it works</li><li>About us</li><li>our partners</li><li>Blog</li>
  </ul>
  <ul class="contact">
    <li><span class="ico"><svg viewBox="0 0 24 24"><path fill="#c62232" d="M12 1C7.6 1 4 4.6 4 9c0 6 8 14 8 14s8-8 8-14c0-4.4-3.6-8-8-8z"/><circle cx="12" cy="9" r="3" fill="#fff"/></svg></span><span>lorem ipsum is a dummy<br>text</span></li>
    <li><span class="ico"><svg viewBox="0 0 24 24"><path fill="#c62232" d="M6.6 2.5l3 3.5-2 2.5c1.2 2.8 3.2 4.8 6 6l2.5-2 3.5 3-2 3.5C10 19 5 14 3 5.5z"/></svg></span><span>123 456 789</span></li>
    <li><span class="ico"><svg viewBox="0 0 24 24" fill="none" stroke="#c62232" stroke-width="2"><rect x="3" y="5" width="18" height="14" rx="2"/><path d="M3 7l9 6 9-6"/></svg></span><span>info@quarrynest.com</span></li>
  </ul>
  <div class="partners">
    <h2>PARTNERS</h2>
    <div class="badge-a" role="img" aria-label="Partner badge"><span></span><span></span></div>
    <div class="badge-b" role="img" aria-label="Partner badge"><span class="disc"></span><span class="bar"></span></div>
  </div>
</footer>
<div class="copyright">© <strong>QUARRYNEST</strong>- 2016. All Rights Reserved.</div>

</body>
</html>
```